KEENARC™ by TALVEN GOLF Squarespace website design

I am looking to have the website look and feel designed. I will attach all the initial content and some other sites I like for inspiration. https://www.pelmorav.com/ https://quindrelo.com/
This is the top bar nav
KEENARC™ by TALVEN GOLF logo
Center: Home | Process | Technology | The Fit | Stroke Map | Testimonials | About
Right: [Start My Fitting] (gold CTA button)

Target Market(s)

Upscale Golfers

Industry/Entity Type

Golf and Technology

```html
<!DOCTYPE html>
<html lang="en">
<head>
<meta charset="utf-8">
<title>KEENARC™ by TALVEN GOLF</title>
<link href="https://fonts.googleapis.com/css2?family=Orbitron:wght@500;700&family=Roboto:ital,wght@0,400;0,500;0,700;1,400&display=swap" rel="stylesheet">
<style>
:root{
  --gold:#fccb06;
  --gold-deep:#d9a800;
  --ink:#0d0b05;
  --white:#ffffff;
  --panel-text:#3a2f00;
}
*{box-sizing:border-box;margin:0;padding:0}
html,body{width:1200px;height:4573px;overflow:hidden}
body{background:var(--ink);color:var(--white);font-family:'Roboto',sans-serif;position:relative}
.abs{position:absolute}
.display{font-family:'Orbitron',sans-serif;font-weight:700;letter-spacing:1px}
.gold{color:var(--gold)}
.thin{font-weight:500}

.hero-photo{left:0;top:0;width:1200px;height:660px;background:radial-gradient(ellipse 320px 420px at 600px 360px,#6b5a3a 0%,#2e2516 45%,#0a0804 80%)}
.brand{left:144px;top:26px;display:flex;align-items:center;gap:14px}
.brand-dot{width:40px;height:40px;border-radius:50%;background:var(--gold)}
.brand-name{font-family:'Orbitron',sans-serif;font-weight:700;font-size:33px;line-height:1;color:var(--white)}
.brand-sub{font-family:'Orbitron',sans-serif;font-weight:700;font-size:11px;letter-spacing:7px;color:var(--white);margin-top:6px}
.cta-top{left:844px;top:32px;width:211px;height:38px;background:var(--gold);color:#111;font-weight:500;font-size:15px;display:flex;align-items:center;justify-content:center}
.nav{left:184px;top:110px;width:956px;height:40px;background:rgba(20,18,12,.85);display:flex;align-items:center;font-size:15px;font-weight:500}
.nav a{color:var(--white);text-decoration:none;padding:0 19px;height:40px;display:flex;align-items:center}
.nav a.active{background:var(--gold);color:#111;margin-left:15px}

.panel{left:144px;width:912px}
.panel svg{position:absolute;left:0;top:0}
.hero-title{left:144px;width:912px;text-align:center;color:#111}
.hero-lead{left:250px;width:700px;text-align:center;font-size:16px;font-weight:500;line-height:29px;color:#111}
.hero-body{left:210px;width:780px;text-align:center;font-size:14px;line-height:26px;color:var(--panel-text)}
.btn-dark{background:#111;color:var(--white);font-weight:700;font-size:14px;display:flex;align-items:center;justify-content:center}
.note{left:144px;width:912px;text-align:center;font-style:italic;font-size:14px;color:#5a4a00}

.section-title{left:0;width:1200px;text-align:center;font-size:42px}
.section-sub{left:0;width:1200px;text-align:center;font-size:17px;font-weight:500}
.feature h3{font-size:16px;font-weight:500;text-decoration:underline;margin-bottom:14px}
.feature p{font-size:15px;line-height:28px;color:#eee}
.feature.right{text-align:right}
.emblem-art{left:440px;top:1530px;width:320px;height:330px;border-radius:40px;background:radial-gradient(ellipse 150px 160px at 50% 45%,#5a4608 0%,#2a2105 55%,rgba(13,11,5,0) 100%)}
.icon-ring{width:76px;height:76px;border:3px solid var(--gold);border-radius:50%;display:flex;align-items:center;justify-content:center;background:var(--ink)}

.how-photo{left:0;top:2059px;width:422px;height:524px;background:radial-gradient(ellipse 160px 260px at 140px 240px,#3a3a38 0%,#161614 55%,#050505 100%)}
.step{display:flex;gap:16px}
.step-num{width:46px;height:46px;border-radius:50%;background:var(--gold);color:#111;font-weight:700;font-size:17px;display:flex;align-items:center;justify-content:center;flex:none}
.step h4{font-size:16px;font-weight:700;margin-bottom:6px;white-space:nowrap}
.step p{font-size:15px;line-height:28px;color:#ddd}
.btn-gold{background:var(--gold);color:#111;font-weight:500;font-size:15px;display:flex;align-items:center;justify-content:center}
.pill{height:213px;border:2px solid var(--gold);border-radius:107px;display:flex;align-items:center;gap:36px;padding-left:38px;background:var(--ink)}
.pill-art{width:100px;height:100px;border-radius:50%;background:radial-gradient(circle,#4a3b08,#1a1505);flex:none}
.pill p{font-size:16px;line-height:29px}

.card{top:3121px;width:280px;height:346px;border-radius:18px;overflow:hidden}
.card.sel{border:6px solid var(--gold)}
.quote{top:3502px;width:220px;text-align:center;font-style:italic;font-size:15px;line-height:26px}
.who{top:3586px;width:280px;text-align:center;color:var(--gold);font-weight:700;font-size:15px}
.arrow{top:3274px;width:42px;height:42px;border:2px solid #777;border-radius:50%;display:flex;align-items:center;justify-content:center}

.foot-brand{left:0;width:1200px;top:4228px;text-align:center}
.foot-tag{left:0;width:1200px;top:4379px;text-align:center;font-size:19px}
.foot-legal{left:0;width:1200px;top:4430px;text-align:center;font-size:15px}
.socials{left:540px;top:4466px;display:flex;gap:10px}
.socials span{width:35px;height:35px;border:2px solid var(--white);border-radius:50%}
</style>
</head>
<body>

<div class="abs hero-photo" role="img" aria-label="Sepia photo of a golfer mid-swing with a glowing gold motion trail"></div>
<div class="abs brand">
  <span class="brand-dot"></span>
  <div><div class="brand-name">KEENARC™</div><div class="brand-sub">BY TALVEN GOLF</div></div>
</div>
<div class="abs cta-top">START MY FITTING</div>
<nav class="abs nav">
  <a class="active">HOME</a><a>PROCESS</a><a>TECHNOLOGY</a><a>THE FIT</a><a>STROKE MAP</a><a>TESTIMONIALS</a><a>ABOUT</a>
</nav>

<svg class="abs" style="left:0;top:560px" width="1200" height="160" viewBox="0 0 1200 160">
  <path d="M0 60 Q80 80 144 100" stroke="var(--gold)" stroke-width="3" fill="none"/>
  <path d="M1056 100 Q1130 80 1200 52" stroke="var(--gold)" stroke-width="3" fill="none"/>
</svg>

<div class="abs panel" style="top:559px;height:723px">
  <svg width="912" height="723" viewBox="0 0 912 723"><path d="M22 0 Q456 190 890 0 Q912 0 912 22 L912 701 Q912 723 890 723 Q456 533 22 723 Q0 723 0 701 L0 22 Q0 0 22 0Z" fill="var(--gold)"/></svg>
</div>
<h1 class="abs hero-title display" style="top:718px;font-size:44px;line-height:58px">YOUR SWING.<br><span class="thin">PERFECTED BY AI.</span></h1>
<p class="abs hero-lead" style="top:852px">Welcome to KEENARC™ by TALVEN GOLF — the world’s first fully automated, AI-powered club-fitting system that engineers your perfect bag from data, not</p>
<p class="abs hero-body" style="top:921px">Every golfer’s swing is unique — and so should be every club in your bag. KEENARC’s AI engine analyzes your swing data, tempo, and ball-flight tendencies, running millions of potential combinations of heads, shafts, and grips across all major OEMs. It isolates the setup that maximizes your distance, consistency, and dispersion — a mathematicallyoptimized build designed for your exact Stroke Map. From</p>
<div class="abs btn-dark" style="left:482px;top:1064px;width:236px;height:50px">START YOUR AI FITTING</div>
<p class="abs note" style="top:1130px">No payment required. Receive your personalized Stroke Map Report instantly.</p>

<h2 class="abs section-title display" style="top:1355px">WHY <span class="gold thin">KEENARC?</span></h2>
<p class="abs section-sub" style="top:1432px">AI Fitting Built for Golfers Who Expect Proof.</p>

<div class="abs emblem-art" role="img" aria-label="Large gold brand emblem illustration connecting the four feature icons"></div>
<div class="abs icon-ring" style="left:407px;top:1553px"><svg width="34" height="34" viewBox="0 0 34 34" fill="none" stroke="var(--gold)" stroke-width="2"><path d="M10 30V4l14 6-14 6"/><ellipse cx="17" cy="30" rx="12" ry="3"/></svg></div>
<div class="abs icon-ring" style="left:748px;top:1553px"><svg width="34" height="34" viewBox="0 0 34 34" fill="none" stroke="var(--gold)" stroke-width="2"><rect x="3" y="5" width="28" height="19" rx="2"/><path d="M12 30h10M17 24v6"/></svg></div>
<div class="abs icon-ring" style="left:472px;top:1738px"><svg width="34" height="34" viewBox="0 0 34 34" fill="none" stroke="var(--gold)" stroke-width="2"><circle cx="17" cy="17" r="14"/><path d="M17 8v9l6 4"/></svg></div>
<div class="abs icon-ring" style="left:651px;top:1738px"><svg width="34" height="34" viewBox="0 0 34 34" fill="none" stroke="var(--gold)" stroke-width="2"><circle cx="17" cy="17" r="14"/><path d="M10 17l5 5 9-10"/></svg></div>

<div class="abs feature" style="left:146px;top:1553px;width:250px"><h3>Smarter than human fitting</h3><p>Machine learning, biomechanics, and physics replace guesswork.</p></div>
<div class="abs feature" style="left:857px;top:1553px;width:210px"><h3>Millions of simulations</h3><p>Every major OEM modeled shafts, lofts, grips, and geometry</p></div>
<div class="abs feature right" style="left:250px;top:1736px;width:203px"><h3>Faster than a session</h3><p>Five-minute digital fitting, instant results.</p></div>
<div class="abs feature" style="left:761px;top:1736px;width:240px"><h3>Portable confidence</h3><p>Your Stroke Map Report travels with you to any builder</p></div>

<svg class="abs" style="left:0;top:1960px" width="1200" height="80" viewBox="0 0 1200 80">
  <path d="M150 50 Q600 0 1050 5" stroke="var(--gold)" stroke-width="3" fill="none"/>
  <path d="M0 0 Q200 60 600 68 Q1000 60 1200 0" stroke="var(--gold-deep)" stroke-width="3" fill="none"/>
</svg>

<div class="abs how-photo" role="img" aria-label="Golfer in dark clothing finishing a swing on a black background"></div>
<h2 class="abs section-title display" style="top:2142px">HOW <span class="gold thin">IT WORKS?</span></h2>
<div class="abs step" style="left:146px;top:2266px;width:300px"><div class="step-num">01</div><div><h4>Input Your Stroke Map</h4><p>Tempo, distances, and goals.</p></div></div>
<div class="abs step" style="left:493px;top:2266px;width:270px"><div class="step-num">02</div><div><h4>AI Simulation Engine</h4><p>Millions of builds tested<br>in seconds.</p></div></div>
<div class="abs step" style="left:808px;top:2266px;width:270px"><div class="step-num">03</div><div><h4>Get Your Report</h4><p>Specs and gapping<br>optimized for your game</p></div></div>
<div class="abs btn-gold" style="left:495px;top:2396px;width:210px;height:36px">SEE THE PROCESS</div>

<svg class="abs" style="left:0;top:2590px" width="1200" height="120" viewBox="0 0 1200 120">
  <path d="M0 92 Q70 70 150 60" stroke="var(--gold)" stroke-width="3" fill="none"/>
  <path d="M1050 60 Q1130 70 1200 95" stroke="var(--gold)" stroke-width="3" fill="none"/>
  <path d="M585 50 H615" stroke="var(--gold)" stroke-width="2"/>
</svg>
<div class="abs pill" style="left:146px;top:2535px;width:442px"><div class="pill-art" role="img" aria-label="Gold line illustration of a golfer"></div><p>Designed from 40 Million<br>Swings and Counting</p></div>
<div class="abs pill" style="left:611px;top:2535px;width:443px"><div class="pill-art" role="img" aria-label="Gold line illustration of a golfer swinging"></div><p>Every KEENARC fit is backed<br>by real player data, OEM<br>R&amp;D, and physics-based<br>simulation</p></div>

<h2 class="abs section-title display" style="top:2903px">PROOF <span class="gold thin">IN PERFORMANCE</span></h2>
<p class="abs section-sub" style="top:2992px;font-size:20px">Real Golfers. Real Results.</p>
<p class="abs section-sub" style="top:3035px;font-size:20px">Validated by data. Proven on the course</p>

<div class="abs arrow" style="left:61px"><svg width="14" height="14" viewBox="0 0 14 14" fill="none" stroke="#999" stroke-width="2"><path d="M9 2L4 7l5 5"/></svg></div>
<div class="abs arrow" style="left:1097px"><svg width="14" height="14" viewBox="0 0 14 14" fill="none" stroke="#999" stroke-width="2"><path d="M5 2l5 5-5 5"/></svg></div>

<div class="abs card sel" style="left:146px;background:linear-gradient(160deg,#20301c,#0c120a 60%,#5e7a8c)" role="img" aria-label="Golfer in light blue top finishing a swing against a dark background"></div>
<div class="abs card" style="left:460px;background:linear-gradient(180deg,#c6d7e0 0%,#6f8f4a 55%,#3f6b23 100%)" role="img" aria-label="Golfer swinging on a sunny green fairway"></div>
<div class="abs card" style="left:774px;background:linear-gradient(160deg,#2a3a14,#7a9a3a 55%,#c9b68a)" role="img" aria-label="Golfer crouching to read a green, holding a club"></div>

<p class="abs quote" style="left:176px">“Picked up 19 yards on my 7-iron and cut my dispersion in half. Pure data magic.”</p>
<p class="abs quote" style="left:490px">“My KEENARC specs matched what my Pelmorav fitter built — but I never left home.”</p>
<p class="abs quote" style="left:804px">“It’s like having a Tour-level engineer model your game in real time.”</p>
<p class="abs who" style="left:146px">Dalen R., 9 Handicap</p>
<p class="abs who" style="left:460px">M. Ostrava, Scratch Player</p>
<p class="abs who" style="left:774px">Priya L., 4Handicap</p>

<div class="abs panel" style="top:3692px;height:529px">
  <svg width="912" height="529" viewBox="0 0 912 529"><path d="M22 0 Q456 150 890 0 Q912 0 912 22 L912 507 Q912 529 890 529 Q456 379 22 529 Q0 529 0 507 L0 22 Q0 0 22 0Z" fill="var(--gold)"/></svg>
</div>
<h2 class="abs hero-title display" style="top:3876px;font-size:42px">BETTER FIT. <span class="thin">BETTER SCORE.</span></h2>
<p class="abs hero-title" style="top:3945px;font-size:23px;font-weight:500">Five minutes to a custom AI fit built from your data</p>
<div class="abs btn-dark" style="left:482px;top:4016px;width:236px;height:50px">START MY KEENARC NOW</div>

<div class="abs foot-brand">
  <div style="width:44px;height:44px;border-radius:50%;background:var(--gold);margin:0 auto 18px"></div>
  <div class="brand-name" style="font-size:40px">KEENARC™</div>
  <div class="brand-sub" style="font-size:13px;letter-spacing:9px;margin-top:8px">BY TALVEN GOLF</div>
</div>
<p class="abs foot-tag">KEENARC™ by TALVEN GOLF · Precision Engineered. AI Perfected</p>
<p class="abs foot-legal">© 2025 Companyname.All Rights Reserved &nbsp;|&nbsp; Privacy Policy &nbsp;|&nbsp; Terms of use</p>
<div class="abs socials"><span></span><span></span><span></span></div>

</body>
</html>
```